Zentrova - Creative Automation

We are a software house for Audio Visual Systems integration/automation and home automation. we develop innovative software to automate a variety of devices mainly related to audio visuals and we design touch panel user interfaces to control these systems.

We would like to see designs that stick to our colours and theme, which you can find on our webpage www.zentrova.com.au

The final design should communicate touch panels, innovation, software and automation.

Industry/Entity Type

Software

Requirements
Must have
• The business card must show the following information:
Name example : Derek Malloway
Qualification example: B Eng ICT(CompSys) Dip EngPrac
Title example : Control Systems Programmer
Mobile Phone, Company phone, Email address ,Company website

```html
<!DOCTYPE html>
<html lang="en">
<head>
<meta charset="utf-8">
<title>Zentrova - Creative Automation · Business Card</title>
<link rel="stylesheet" href="https://fonts.googleapis.com/css2?family=Montserrat:wght@400;500;700&display=swap">
<style>
  :root {
    --backdrop: #e7e9e6;
    --card-dark: #414b52;
    --card-light: #f4f5f5;
    --brand-blue: #3d87c9;
    --brand-green: #2ea55a;
    --brand-orange: #f2a93b;
    --ink-white: #ffffff;
    --shadow: rgba(0, 0, 0, 0.18);
  }
  * { margin: 0; padding: 0; box-sizing: border-box; }
  html, body {
    width: 1200px;
    height: 800px;
    overflow: hidden;
    background: var(--backdrop);
    font-family: "Montserrat", sans-serif;
  }
  .canvas { position: relative; width: 1200px; height: 800px; }

  .card {
    position: absolute;
    width: 560px;
    height: 300px;
    box-shadow: 0 8px 22px var(--shadow);
  }

  /* Front side */
  .card-front {
    left: 150px;
    top: 140px;
    background: var(--card-dark);
  }
  .brand {
    position: absolute;
    left: 50%;
    top: 50%;
    transform: translate(-50%, -50%);
    display: flex;
    flex-direction: column;
    align-items: flex-end;
  }
  .brand-row { display: flex; align-items: center; gap: 16px; }
  .brand-square {
    width: 58px;
    height: 58px;
    background: var(--brand-green);
  }
  .brand-name {
    font-weight: 700;
    font-size: 44px;
    line-height: 1;
    color: var(--brand-blue);
    letter-spacing: 0.5px;
  }
  .brand-tagline {
    margin-top: 4px;
    font-weight: 700;
    font-size: 11px;
    color: var(--ink-white);
  }

  /* Back side */
  .card-back {
    left: 500px;
    top: 420px;
    background: var(--card-light);
  }
  .tile {
    position: absolute;
    display: flex;
    align-items: center;
    gap: 12px;
    padding: 0 14px;
    color: var(--ink-white);
    font-size: 12px;
    font-weight: 500;
  }
  .tile svg { flex: none; width: 16px; height: 16px; }
  .tile-blue { background: var(--brand-blue); }
  .tile-green { background: var(--brand-green); }
  .tile-orange { background: var(--brand-orange); }

  .name-tile {
    left: 28px; top: 40px; width: 236px; height: 96px;
    flex-direction: column;
    align-items: flex-start;
    justify-content: center;
    gap: 2px;
    padding-left: 18px;
  }
  .person-name { font-size: 17px; font-weight: 500; letter-spacing: 0.5px; }
  .person-name strong { font-weight: 700; }
  .person-title { font-size: 11.5px; font-weight: 400; }

  .back-brand {
    position: absolute;
    left: 290px;
    top: 62px;
    align-items: flex-end;
    display: flex;
    flex-direction: column;
  }
  .back-brand .brand-row { gap: 10px; }
  .back-brand .brand-square { width: 36px; height: 36px; }
  .back-brand .brand-name { font-size: 28px; }
  .back-brand .brand-tagline { font-size: 7.5px; color: var(--card-dark); margin-top: 2px; }

  .tile-mobile { left: 28px; top: 150px; width: 160px; height: 52px; }
  .tile-office { left: 198px; top: 150px; width: 160px; height: 52px; }
  .tile-address { left: 368px; top: 150px; width: 164px; height: 52px; font-size: 10.5px; line-height: 1.25; }
  .tile-web { left: 28px; top: 214px; width: 256px; height: 52px; }
  .tile-email { left: 294px; top: 214px; width: 238px; height: 52px; }
</style>
</head>
<body>
<main class="canvas">

  <section class="card card-front" aria-label="Business card front">
    <div class="brand">
      <div class="brand-row">
        <span class="brand-square"></span>
        <span class="brand-name">zentrova</span>
      </div>
      <span class="brand-tagline">Creative Automation</span>
    </div>
  </section>

  <section class="card card-back" aria-label="Business card back">
    <div class="tile tile-blue name-tile">
      <span class="person-name"><strong>DEREK</strong> MALLOWAY</span>
      <span class="person-title">Control Systems Programmer</span>
    </div>

    <div class="back-brand">
      <div class="brand-row">
        <span class="brand-square"></span>
        <span class="brand-name">zentrova</span>
      </div>
      <span class="brand-tagline">Creative Automation</span>
    </div>

    <div class="tile tile-green tile-mobile">
      <svg viewBox="0 0 16 16" aria-hidden="true"><rect x="4" y="1" width="8" height="14" rx="1.5" fill="none" stroke="#fff" stroke-width="1.5"/><circle cx="8" cy="12.5" r="0.9" fill="#fff"/></svg>
      <span>0412 558 904</span>
    </div>

    <div class="tile tile-orange tile-office">
      <svg viewBox="0 0 16 16" aria-hidden="true"><path d="M3.2 1.5l2.6 0.4 1 3-1.6 1.3a9 9 0 0 0 4.6 4.6l1.3-1.6 3 1 0.4 2.6c-0.5 1-1.6 1.7-2.8 1.6C6.2 13.9 2.1 9.8 1.6 4.3 1.5 3.1 2.2 2 3.2 1.5z" fill="#fff"/></svg>
      <span>0239 486 120</span>
    </div>

    <div class="tile tile-green tile-address">
      <svg viewBox="0 0 16 16" aria-hidden="true"><path d="M8 1a5 5 0 0 0-5 5c0 3.6 5 9 5 9s5-5.4 5-9a5 5 0 0 0-5-5z" fill="#fff"/><circle cx="8" cy="6" r="1.8" fill="var(--brand-green)"/></svg>
      <span>18 Millbrook Lane<br>Kestrelton, NSW, 2790</span>
    </div>

    <div class="tile tile-blue tile-web">
      <svg viewBox="0 0 16 16" aria-hidden="true"><g fill="none" stroke="#fff" stroke-width="1.2"><circle cx="8" cy="8" r="6.5"/><ellipse cx="8" cy="8" rx="2.8" ry="6.5"/><path d="M1.5 8h13M2.6 4.6h10.8M2.6 11.4h10.8"/></g></svg>
      <span>www.zentrova.com.au</span>
    </div>

    <div class="tile tile-orange tile-email">
      <svg viewBox="0 0 16 16" aria-hidden="true"><rect x="1.5" y="3.5" width="13" height="9" fill="#fff"/><path d="M1.5 3.5L8 9l6.5-5.5" fill="none" stroke="var(--brand-orange)" stroke-width="1.2"/></svg>
      <span>info@zentrova.com.au</span>
    </div>
  </section>

</main>
</body>
</html>
```